Business Card Design Project

I need a business card designed from scratch. I have an existing logo that I can upload in Illustrator for modification or redesign.

The Company is called Rank Harbor http://rankharbor.com.au and we provide Search Engine Optimization services to Australian businesses. The current logo signifies an increase in visitors, profits etc...

There are no restrictions as to the redesign - colours, style etc are all open to change.

Cards will be full colour and one sided printed at http://www.printlorvex.com.au so check their requirements for file format and sizes etc.

I will expect all original files upon completion of project.

Target Market(s)

Any business with a web site looking to improve their search engine rankings

Industry/Entity Type

Business

Requirements
Must have
• I like modern, sleek designs. Clean, not fussy, uncluttered.

```html
<!DOCTYPE html>
<html lang="en">
<head>
<meta charset="utf-8">
<title>Rank Harbor — Business Card</title>
<link rel="stylesheet" href="https://fonts.googleapis.com/css2?family=Open+Sans:wght@400;600;700&display=swap">
<style>
  :root {
    --backdrop: #e8e5e1;
    --card-black: #050505;
    --brand-blue: #1a74b9;
    --logo-blue: #2b7fc3;
    --accent-yellow: #f6c417;
    --text-white: #ffffff;
    --text-soft: #eaf2fa;
  }
  * { box-sizing: border-box; margin: 0; padding: 0; }
  html, body {
    width: 1200px; height: 460px; overflow: hidden;
    background: var(--backdrop);
    font-family: "Open Sans", Arial, sans-serif;
  }
  .canvas { position: relative; width: 1200px; height: 460px; }
  .card {
    position: absolute; top: 75px; width: 541px; height: 309px;
    border-radius: 14px; overflow: hidden; background: var(--card-black);
    box-shadow: 0 4px 10px rgba(0,0,0,0.25);
  }
  .card--front { left: 45px; }
  .card--back { left: 613px; }

  .front-brand {
    position: absolute; left: 0; top: 0; width: 292px; height: 100%;
    display: flex; align-items: center; justify-content: center;
  }
  .divider {
    position: absolute; left: 292px; top: 0; width: 3px; height: 100%;
    background: var(--accent-yellow);
  }
  .contact-panel {
    position: absolute; left: 295px; top: 0; right: 0; height: 100%;
    background: var(--brand-blue); color: var(--text-white);
    padding: 56px 0 0 14px;
  }
  .person-name { font-size: 17px; font-weight: 700; line-height: 1.2; }
  .person-title { font-size: 13px; color: var(--text-soft); margin-top: 1px; }
  .contact-list { list-style: none; margin-top: 20px; }
  .contact-list li {
    display: flex; align-items: center; gap: 6px;
    font-size: 13px; line-height: 18px;
  }
  .contact-list svg { width: 9px; height: 9px; fill: var(--text-white); flex: none; }
  .address { font-size: 13px; line-height: 18px; margin-top: 16px; }

  .wordmark {
    display: flex; align-items: center; gap: 10px;
  }
  .wordmark-dot {
    width: 14px; height: 14px; border-radius: 50%; background: var(--accent-yellow);
  }
  .wordmark-name {
    font-size: 28px; font-weight: 700; color: var(--logo-blue); letter-spacing: -0.3px;
  }
  .back-content {
    position: absolute; inset: 0;
    display: flex; flex-direction: column; align-items: center; justify-content: center;
    padding-top: 14px;
  }
  .back-content .wordmark-name { font-size: 34px; }
  .back-url {
    margin-top: 40px; font-size: 13px; letter-spacing: 2.6px; color: var(--text-white);
  }
</style>
</head>
<body>
<div class="canvas">
  <section class="card card--front">
    <div class="front-brand">
      <div class="wordmark">
        <span class="wordmark-dot"></span>
        <span class="wordmark-name">Rank Harbor</span>
      </div>
    </div>
    <div class="divider"></div>
    <div class="contact-panel">
      <p class="person-name">Your Name</p>
      <p class="person-title">Title</p>
      <ul class="contact-list">
        <li><svg viewBox="0 0 10 10"><path d="M2 0.5 3.8 2.6 2.8 3.8C3.5 5.2 4.8 6.5 6.2 7.2L7.4 6.2 9.5 8 8.4 9.5C4.5 9.2 0.8 5.5 0.5 1.6Z"/></svg>098 765 4321</li>
        <li><svg viewBox="0 0 10 10"><path d="M2.5 0h5a.8.8 0 0 1 .8.8v8.4a.8.8 0 0 1-.8.8h-5a.8.8 0 0 1-.8-.8V.8A.8.8 0 0 1 2.5 0Zm.6 1.5v5.5h3.8V1.5Z"/></svg>098 765 4321</li>
        <li><svg viewBox="0 0 10 10"><path d="M0 2h10v1L5 6 0 3Zm0 2.2 5 3 5-3V8H0Z"/></svg>enquiry@rankharbor.com.au</li>
        <li><svg viewBox="0 0 10 10"><circle cx="5" cy="5" r="4.5"/></svg>www.rankharbor.com.au</li>
      </ul>
      <p class="address">00Floor Street, City Name<br>State Name, Contry Name</p>
    </div>
  </section>

  <section class="card card--back">
    <div class="back-content">
      <div class="wordmark">
        <span class="wordmark-dot"></span>
        <span class="wordmark-name">Rank Harbor</span>
      </div>
      <p class="back-url">www.rankharbor.com.au</p>
    </div>
  </section>
</div>
</body>
</html>
```